Graphic Design Set for Banner Ads - Sizes and Specs for Pixmora

We need a set of 6 ads of the following sizes created for Pixmora:

Medium rectangle: 300×250
Leaderboard: 728×90
Wide skyscraper: 160×600
Large rectangle: 300x600
Mobile leaderboard: 320×50

Here are the Formatting Guidelines (WEB ADS): https://help.pixmora.example/hc/en-us/articles/583920147-Ad-Content-and-Format-Guidelines

Here is the website: https://valmiraliving.example/

Here are some words for the ad - feel free to use creative liberties if you have something better or need less words.

1. The Future of Aging is Here

2. Dementia At-Home Care

3. Benefits of an Assisted Living from the Privacy of Your Home - link to

4. Idaho's New Senior Care Option

5. The Security of Senior Living from the Comfort of Your Home

I have the images for all website photos, if you need more images, please let me know.

Target Market(s)

Women age 55+

Industry/Entity Type

Graphic Design

Requirements
Must have
• Incorporate website imagery as much as possible
Should not have
• a feeling of helplessness, old, etc.

```html
<!DOCTYPE html>
<html lang="en">
<head>
<meta charset="utf-8">
<title>Valmira Living — Banner Ad Set</title>
<link rel="stylesheet" href="https://fonts.googleapis.com/css2?family=Alike&family=Montserrat:wght@500;600;700&display=swap">
<style>
:root{
  --page:#ffffff;
  --ember-dark:#2a140b;
  --ember-mid:#5a2e17;
  --ember-glow:#8a4a1f;
  --ember-text:#e0892a;
  --rose:#c77aa8;
  --rose-soft:#d9a8b8;
  --taupe:#bfae9a;
  --sand:#cdb79a;
  --ink:#463c3c;
  --olive:#6d6a1c;
  --ocean:#1a5a9e;
  --teal:#1f9a95;
  --lagoon:#2bb09a;
  --gold:#e8d46a;
  --white:#ffffff;
  --serif:"Alike", Georgia, serif;
  --sans:"Montserrat", Arial, sans-serif;
}
*{margin:0;padding:0;box-sizing:border-box}
html,body{width:1200px;height:1171px;overflow:hidden;background:var(--page)}
.stage{position:relative;width:1500px;height:1464px;transform:scale(.8);transform-origin:0 0}
.ad{position:absolute;overflow:hidden;color:var(--white)}
.photo{position:absolute;inset:0}
.ember .photo{background:radial-gradient(ellipse at 70% 30%,var(--ember-glow) 0%,var(--ember-mid) 40%,var(--ember-dark) 100%)}
.memory .photo{background:linear-gradient(180deg,#b9a2a8 0%,var(--rose-soft) 40%,var(--rose) 100%)}
.memory.wide .photo{background:linear-gradient(90deg,var(--rose) 0%,var(--rose-soft) 55%,var(--taupe) 100%)}
.care .photo{background:linear-gradient(160deg,var(--rose) 0%,var(--rose-soft) 45%,var(--sand) 100%)}
.care.wide .photo{background:linear-gradient(90deg,var(--rose) 0%,var(--rose-soft) 50%,var(--sand) 100%)}
.haven .photo{background:linear-gradient(180deg,var(--ocean) 0%,var(--teal) 50%,var(--lagoon) 100%)}
.haven.wide .photo{background:linear-gradient(90deg,var(--ocean) 0%,var(--teal) 40%,var(--lagoon) 100%)}
.t{position:absolute;line-height:1;white-space:nowrap}
.logo{font-family:var(--sans);font-weight:500;letter-spacing:.06em;color:var(--white);font-size:17px}
.logo.dark{color:var(--ink)}
.caps{font-family:var(--sans);font-weight:700;letter-spacing:.12em;text-transform:uppercase}
.script{font-family:var(--serif)}
.orange{color:var(--ember-text)}
.gold{color:var(--gold)}
.ink{color:var(--ink)}
.olive{color:var(--olive)}
.right{text-align:right}
</style>
</head>
<body>
<main class="stage">

<!-- Set 1: The future of aging -->
<section class="ad ember" style="left:32px;top:32px;width:190px;height:158px">
  <div class="photo" role="img" aria-label="Stocking feet resting by a warm fireplace"></div>
  <div class="t logo" style="left:12px;top:10px;font-size:13px">VALMIRA</div>
  <div class="t caps" style="left:12px;top:65px;font-size:11px">The</div>
  <div class="t script orange" style="left:12px;top:76px;font-size:24px">future of aging</div>
  <div class="t caps right" style="right:12px;top:104px;font-size:11px">Is here</div>
</section>
<section class="ad ember" style="left:32px;top:203px;width:190px;height:380px">
  <div class="photo" role="img" aria-label="Stocking feet resting by a warm fireplace"></div>
  <div class="t caps" style="left:12px;top:120px;font-size:13px">The</div>
  <div class="t script orange" style="left:12px;top:134px;font-size:34px;line-height:.92">future<br>of aging</div>
  <div class="t caps" style="left:15px;top:198px;font-size:12px">Is here</div>
  <div class="t logo" style="right:14px;bottom:18px;font-size:19px">VALMIRA</div>
</section>
<section class="ad ember" style="left:235px;top:203px;width:102px;height:380px">
  <div class="photo" role="img" aria-label="Stocking feet resting by a warm fireplace"></div>
  <div class="t logo" style="left:12px;top:12px;font-size:16px">VALMIRA</div>
  <div class="t caps" style="left:12px;top:72px;font-size:11px">The</div>
  <div class="t script orange" style="left:12px;top:88px;font-size:24px;line-height:.95">future<br>of<br>aging</div>
  <div class="t caps" style="left:13px;top:168px;font-size:11px">Is here</div>
</section>
<section class="ad ember wide" style="left:32px;top:596px;width:462px;height:72px">
  <div class="photo" role="img" aria-label="Stocking feet resting by a warm fireplace"></div>
  <div class="t caps" style="left:8px;top:8px;font-size:13px">The</div>
  <div class="t script orange" style="left:7px;top:20px;font-size:27px">future of aging</div>
  <div class="t caps" style="left:138px;top:50px;font-size:13px">Is here</div>
  <div class="t logo" style="right:16px;top:28px;font-size:19px">VALMIRA</div>
</section>
<section class="ad ember wide" style="left:32px;top:681px;width:203px;height:31px">
  <div class="photo" role="img" aria-label="Stocking feet resting by a warm fireplace"></div>
  <div class="t caps" style="left:8px;top:9px;font-size:7px">The</div>
  <div class="t script orange" style="left:27px;top:4px;font-size:14px">future of aging</div>
  <div class="t caps" style="left:104px;top:21px;font-size:6px">Is here</div>
  <div class="t logo" style="right:8px;top:10px;font-size:8px">VALMIRA</div>
</section>

<!-- Set 2: Dementia at-home care -->
<section class="ad memory" style="left:519px;top:32px;width:190px;height:158px">
  <div class="photo" role="img" aria-label="Older and younger hands resting together"></div>
  <div class="t logo dark right" style="right:10px;top:8px;font-size:13px">VALMIRA</div>
  <div class="t script" style="left:8px;top:108px;font-size:25px">Dementia</div>
  <div class="t caps ink" style="left:122px;top:116px;font-size:9px;line-height:1.4">At-home<br>&nbsp;&nbsp;care</div>
</section>
<section class="ad memory" style="left:519px;top:203px;width:190px;height:380px">
  <div class="photo" role="img" aria-label="Older and younger hands resting together"></div>
  <div class="t logo right" style="right:14px;top:12px;font-size:17px">VALMIRA</div>
  <div class="t script" style="left:8px;top:76px;font-size:38px">Dementia</div>
  <div class="t caps ink" style="left:10px;top:334px;font-size:10px;line-height:1.4">At-home<br>care</div>
</section>
<section class="ad memory" style="left:722px;top:203px;width:102px;height:380px">
  <div class="photo" role="img" aria-label="Older and younger hands resting together"></div>
  <div class="t logo" style="left:8px;top:12px;font-size:16px">VALMIRA</div>
  <div class="t script" style="left:8px;top:78px;font-size:18px">Dementia</div>
  <div class="t caps ink" style="left:10px;top:100px;font-size:9px;line-height:1.5">At-home<br>care</div>
</section>
<section class="ad memory wide" style="left:519px;top:596px;width:462px;height:72px">
  <div class="photo" role="img" aria-label="Older and younger hands resting together"></div>
  <div class="t script" style="left:16px;top:8px;font-size:36px">Dementia</div>
  <div class="t caps ink" style="left:18px;top:45px;font-size:10px">At-home care</div>
  <div class="t logo" style="right:10px;top:6px;font-size:20px">VALMIRA</div>
</section>
<section class="ad memory wide" style="left:519px;top:681px;width:203px;height:31px">
  <div class="photo" role="img" aria-label="Older and younger hands resting together"></div>
  <div class="t caps ink" style="left:35px;top:3px;font-size:7px">At-home care</div>
  <div class="t script" style="left:7px;top:11px;font-size:18px">Dementia</div>
  <div class="t logo" style="right:8px;top:9px;font-size:10px">VALMIRA</div>
</section>

<!-- Set 3: Benefits of assisted living at home -->
<section class="ad ember" style="left:1006px;top:32px;width:190px;height:158px">
  <div class="photo" role="img" aria-label="Red patterned socks warming by a fireplace"></div>
  <div class="t caps" style="left:102px;top:6px;font-size:10px;line-height:1.4">The<br>benefits<br>of<br>assisted<br>living</div>
  <div class="t script orange right" style="right:10px;top:66px;font-size:30px;line-height:.8">at<br>home</div>
  <div class="t logo" style="left:6px;bottom:10px;font-size:13px">VALMIRA</div>
</section>
<section class="ad ember" style="left:1006px;top:203px;width:190px;height:380px">
  <div class="photo" role="img" aria-label="Red patterned socks warming by a fireplace"></div>
  <div class="t logo" style="left:18px;top:24px;font-size:20px">VALMIRA</div>
  <div class="t caps" style="left:20px;top:100px;font-size:10px">The benefits of</div>
  <div class="t caps" style="left:20px;top:116px;font-size:12px;letter-spacing:.16em">Assisted living</div>
  <div class="t script orange right" style="right:14px;top:128px;font-size:44px;line-height:.8">at<br>home</div>
</section>
<section class="ad ember" style="left:1209px;top:203px;width:102px;height:380px">
  <div class="photo" role="img" aria-label="Red patterned socks warming by a fireplace"></div>
  <div class="t logo" style="left:8px;top:16px;font-size:15px">VALMIRA</div>
  <div class="t caps" style="left:10px;top:50px;font-size:11px;line-height:1.5">The<br>benefits<br>of<br>assisted<br>living</div>
  <div class="t script orange" style="left:8px;top:136px;font-size:32px;line-height:1.05">at<br>home</div>
</section>
<section class="ad ember wide" style="left:1006px;top:596px;width:462px;height:72px">
  <div class="photo" role="img" aria-label="Red patterned socks warming by a fireplace"></div>
  <div class="t caps right" style="right:114px;top:16px;font-size:11px">The benefits of assisted living</div>
  <div class="t script orange right" style="right:114px;top:27px;font-size:30px">at home</div>
  <div class="t logo" style="right:10px;top:33px;font-size:15px">VALMIRA</div>
</section>
<section class="ad ember wide" style="left:1006px;top:681px;width:203px;height:31px">
  <div class="photo" role="img" aria-label="Red patterned socks warming by a fireplace"></div>
  <div class="t caps" style="left:8px;top:4px;font-size:6px">The benefits of assisted living</div>
  <div class="t script orange" style="left:80px;top:12px;font-size:16px">at home</div>
  <div class="t logo" style="right:8px;top:12px;font-size:8px">VALMIRA</div>
</section>

<!-- Set 4: Idaho's new senior care option -->
<section class="ad care" style="left:32px;top:751px;width:190px;height:158px">
  <div class="photo" role="img" aria-label="Caring hands resting on a knit blanket"></div>
  <div class="t logo right" style="right:10px;top:6px;font-size:13px">VALMIRA</div>
  <div class="t caps ink" style="left:8px;top:88px;font-size:11px">Idaho’s new</div>
  <div class="t script ink" style="left:6px;top:100px;font-size:30px">Senior Care</div>
  <div class="t script olive" style="left:6px;top:128px;font-size:22px">Option</div>
</section>
<section class="ad care" style="left:32px;top:922px;width:190px;height:380px">
  <div class="photo" role="img" aria-label="Caring hands resting on a knit blanket"></div>
  <div class="t logo" style="left:6px;top:8px;font-size:17px">VALMIRA</div>
  <div class="t caps ink" style="left:8px;top:196px;font-size:12px">Idaho’s new</div>
  <div class="t script ink" style="left:6px;top:208px;font-size:32px">Senior Care</div>
  <div class="t script olive right" style="right:10px;top:238px;font-size:20px">Option</div>
</section>
<section class="ad care" style="left:235px;top:922px;width:102px;height:380px">
  <div class="photo" role="img" aria-label="Caring hands resting on a knit blanket"></div>
  <div class="t logo" style="left:8px;top:12px;font-size:16px">VALMIRA</div>
  <div class="t caps ink" style="left:8px;top:83px;font-size:8px">Idaho’s new</div>
  <div class="t script ink" style="left:7px;top:94px;font-size:27px;line-height:.98">Senior<br>Care</div>
  <div class="t script olive" style="left:7px;top:148px;font-size:22px">Option</div>
</section>
<section class="ad care wide" style="left:32px;top:1315px;width:462px;height:72px">
  <div class="photo" role="img" aria-label="Caring hands resting on a knit blanket"></div>
  <div class="t caps ink" style="left:22px;top:17px;font-size:11px">Idaho’s new</div>
  <div class="t script olive" style="left:46px;top:30px;font-size:21px">Senior Care Option</div>
  <div class="t logo dark" style="right:8px;top:8px;font-size:18px">VALMIRA</div>
</section>
<section class="ad care wide" style="left:32px;top:1400px;width:203px;height:31px">
  <div class="photo" role="img" aria-label="Caring hands resting on a knit blanket"></div>
  <div class="t caps ink" style="left:7px;top:4px;font-size:7px">Idaho’s new</div>
  <div class="t script olive" style="left:6px;top:12px;font-size:14px">Senior Care Option</div>
  <div class="t logo dark" style="right:8px;top:9px;font-size:10px">VALMIRA</div>
</section>

<!-- Set 5: Security and comfort -->
<section class="ad haven" style="left:519px;top:751px;width:190px;height:158px">
  <div class="photo" role="img" aria-label="Hands joined over a soft blanket, tinted teal"></div>
  <div class="t logo right" style="right:10px;top:10px;font-size:13px">VALMIRA</div>
  <div class="t caps" style="left:7px;top:32px;font-size:11px">The</div>
  <div class="t script gold" style="left:7px;top:44px;font-size:24px">security</div>
  <div class="t caps" style="left:7px;top:74px;font-size:8px;font-weight:600">Of assisted living</div>
  <div class="t caps" style="left:7px;top:97px;font-size:11px">From the</div>
  <div class="t script gold" style="left:7px;top:108px;font-size:24px">comfort</div>
  <div class="t caps" style="left:7px;top:137px;font-size:8px;font-weight:600">Of your own home</div>
</section>
<section class="ad haven" style="left:519px;top:922px;width:190px;height:380px">
  <div class="photo" role="img" aria-label="Hands joined over a soft blanket, tinted teal"></div>
  <div class="t logo right" style="right:10px;top:12px;font-size:15px">VALMIRA</div>
  <div class="t caps" style="left:13px;top:82px;font-size:11px">The</div>
  <div class="t script gold" style="left:13px;top:95px;font-size:28px">security</div>
  <div class="t caps" style="left:13px;top:130px;font-size:8px;font-weight:600">Of assisted living</div>
  <div class="t caps" style="left:13px;top:154px;font-size:11px">From the</div>
  <div class="t script gold" style="left:13px;top:167px;font-size:28px">comfort</div>
  <div class="t caps" style="left:13px;top:199px;font-size:8px;font-weight:600">Of your own home</div>
</section>
<section class="ad haven" style="left:722px;top:922px;width:102px;height:380px">
  <div class="photo" role="img" aria-label="Hands joined over a soft blanket, tinted teal"></div>
  <div class="t logo right" style="right:6px;top:10px;font-size:14px">VALMIRA</div>
  <div class="t caps" style="left:5px;top:58px;font-size:11px">The</div>
  <div class="t script gold" style="left:5px;top:68px;font-size:22px">security</div>
  <div class="t caps" style="left:5px;top:92px;font-size:8px;font-weight:600;line-height:1.6">Of<br>assisted<br>living</div>
  <div class="t caps" style="left:5px;top:144px;font-size:11px">From the</div>
  <div class="t script gold" style="left:5px;top:155px;font-size:22px">comfort</div>
  <div class="t caps" style="left:5px;top:180px;font-size:8px;font-weight:600;line-height:1.6">Of your<br>own home</div>
</section>
<section class="ad haven wide" style="left:519px;top:1315px;width:462px;height:72px">
  <div class="photo" role="img" aria-label="Hands joined over a soft blanket, tinted teal"></div>
  <div class="t logo" style="left:16px;top:31px;font-size:16px">VALMIRA</div>
  <div class="t caps" style="left:119px;top:7px;font-size:12px;font-weight:500">The</div>
  <div class="t script gold" style="left:119px;top:18px;font-size:30px">security</div>
  <div class="t caps" style="left:119px;top:53px;font-size:9px;font-weight:600">Of assisted living</div>
  <div class="t caps" style="left:276px;top:7px;font-size:12px;font-weight:500">From the</div>
  <div class="t script gold" style="left:276px;top:18px;font-size:30px">comfort</div>
  <div class="t caps" style="left:276px;top:53px;font-size:9px;font-weight:600">Of your own home</div>
</section>
<section class="ad haven wide" style="left:519px;top:1400px;width:203px;height:31px">
  <div class="photo" role="img" aria-label="Hands joined over a soft blanket, tinted teal"></div>
  <div class="t logo" style="left:5px;top:11px;font-size:8px">VALMIRA</div>
  <div class="t caps" style="left:60px;top:2px;font-size:5px">The</div>
  <div class="t script gold" style="left:60px;top:8px;font-size:13px">security</div>
  <div class="t caps" style="left:60px;top:22px;font-size:4px">Of assisted living</div>
  <div class="t caps" style="left:126px;top:2px;font-size:5px">From the</div>
  <div class="t script gold" style="left:126px;top:8px;font-size:13px">comfort</div>
  <div class="t caps" style="left:126px;top:22px;font-size:4px">Of your own home</div>
</section>

</main>
</body>
</html>
```